The Merry Hound - Dog Training Business Card Design

I need a business card design for a new dog training company based in Cronulla NSW called The Merry Hound. I run puppy pre school classes, adult dog classes and do one on one training in the person's home.
I have studied for 2 years and use positive reinforcement training methods based on how dogs learn. I believe in communicating with our dogs what we want them to do rather than punish them for behaviours we don't like. I would like to see designs that use the colours that are used in my logo (please see attached)
I would like a simple and classic looking design. I don't want cartoon images of dogs or any animal images or drawings on the card. I have created my logo with this mindset. I am open to the subtle use of a dog's tail, paws or paw print.

Target Market(s)

high end area which is why I want a classic looking design
adults aged 25 and over

Industry/Entity Type

Dog Training

Contact Information for Business Card

Miriam Caslett
ORBIS Trained Professional Dog Trainer
www.themerryhound-example.com.au
0499731628
miriam@themerryhound-example.com.au

Font styles to use
Sans Serif

Colors
ffffff
86cae6
757575

Requirements
Must have
• Logo - I am trying to attach my logo and colour palette but it won't allow me. I will contact the company and upload ASAP.
Should not have
• images of dogs or cartoon drawings

```html
<!DOCTYPE html>
<html lang="en">
<head>
<meta charset="utf-8">
<title>The Merry Hound – Business Cards</title>
<link rel="stylesheet" href="https://fonts.googleapis.com/css2?family=Roboto:wght@300;400;700&display=swap">
<style>
  :root {
    --stage: #ecebe8;
    --card-top: #c3def2;
    --card-bottom: #a9cfec;
    --paw-tint: rgba(255, 255, 255, 0.28);
    --white: #ffffff;
    --grey: #757575;
    --rule: #8a8f94;
  }
  * { margin: 0; padding: 0; box-sizing: border-box; }
  html, body {
    width: 1200px;
    height: 855px;
    overflow: hidden;
    background: var(--stage);
    font-family: "Roboto", Arial, sans-serif;
  }
  .stage {
    position: relative;
    width: 1200px;
    height: 855px;
  }
  .card {
    position: absolute;
    top: 262px;
    width: 540px;
    height: 330px;
    background: linear-gradient(160deg, var(--card-top), var(--card-bottom));
    box-shadow: 0 6px 18px rgba(0, 0, 0, 0.18);
    overflow: hidden;
  }
  .card--front { left: 40px; }
  .card--back { left: 620px; }

  /* Front */
  .paw-decoration {
    position: absolute;
    background: var(--paw-tint);
    border-radius: 40px;
  }
  .paw-decoration--top { top: 22px; right: 22px; width: 130px; height: 110px; }
  .paw-decoration--bottom { bottom: 22px; left: 22px; width: 150px; height: 120px; }

  .brand {
    position: absolute;
    left: 0;
    right: 0;
    top: 118px;
    text-align: center;
  }
  .brand__name {
    font-weight: 300;
    font-size: 46px;
    letter-spacing: 1px;
    color: var(--white);
    line-height: 1;
  }
  .brand__tagline {
    margin-top: 10px;
    font-weight: 400;
    font-size: 12px;
    letter-spacing: 3px;
    color: var(--white);
  }
  .front-web {
    position: absolute;
    left: 0;
    right: 0;
    bottom: 46px;
    text-align: center;
    font-size: 15px;
    color: var(--grey);
  }

  /* Back */
  .back-brand {
    position: absolute;
    left: 30px;
    top: 50px;
    width: 200px;
    font-weight: 300;
    font-size: 34px;
    line-height: 1.05;
    color: var(--white);
  }
  .back-rule {
    position: absolute;
    left: 30px;
    right: 30px;
    top: 160px;
    height: 1px;
    background: var(--rule);
  }
  .contact {
    position: absolute;
    left: 30px;
    top: 180px;
    right: 30px;
  }
  .contact__name {
    font-weight: 700;
    font-size: 22px;
    color: var(--white);
  }
  .contact__title {
    margin-top: 6px;
    font-size: 14px;
    color: var(--grey);
  }
  .contact__list {
    list-style: none;
    margin-top: 16px;
  }
  .contact__item {
    display: flex;
    align-items: center;
    gap: 8px;
    font-size: 14px;
    color: var(--grey);
    margin-bottom: 6px;
  }
  .contact__icon {
    width: 14px;
    height: 14px;
    flex: none;
  }
</style>
</head>
<body>
<main class="stage">

  <section class="card card--front" aria-label="Business card front">
    <div class="paw-decoration paw-decoration--top" role="img" aria-label="Faint paw print decoration"></div>
    <div class="paw-decoration paw-decoration--bottom" role="img" aria-label="Faint paw print decoration"></div>
    <div class="brand">
      <h1 class="brand__name">The Merry Hound</h1>
      <p class="brand__tagline">POSITIVE TRAINING SPECIALIST</p>
    </div>
    <p class="front-web">www.themerryhound-example.com.au</p>
  </section>

  <section class="card card--back" aria-label="Business card back">
    <p class="back-brand">The Merry Hound</p>
    <div class="back-rule"></div>
    <div class="contact">
      <h2 class="contact__name">Miriam Caslett</h2>
      <p class="contact__title">ORBIS Trained Professional Dog Trainer</p>
      <ul class="contact__list">
        <li class="contact__item">
          <svg class="contact__icon" viewBox="0 0 14 14" aria-hidden="true">
            <circle cx="7" cy="7" r="7" fill="#ffffff"/>
            <path d="M4.5 3.5 L6 3.5 L6.6 5.4 L5.7 6.1 Q6.4 7.6 7.9 8.3 L8.6 7.4 L10.5 8 L10.5 9.5 Q6.8 10.2 4.5 7 Q3.8 5.2 4.5 3.5 Z" fill="#757575"/>
          </svg>
          0499731628
        </li>
        <li class="contact__item">
          <svg class="contact__icon" viewBox="0 0 14 14" aria-hidden="true">
            <circle cx="7" cy="7" r="7" fill="#ffffff"/>
            <rect x="3.5" y="4.5" width="7" height="5" fill="none" stroke="#757575" stroke-width="1"/>
            <path d="M3.5 4.5 L7 7.3 L10.5 4.5" fill="none" stroke="#757575" stroke-width="1"/>
          </svg>
          miriam@themerryhound-example.com.au
        </li>
      </ul>
    </div>
  </section>

</main>
</body>
</html>
```